TOVR Enterprise
company business card and envolpe design
TOVR Enterprise -
Creative Brief
Professional
Neeraj Pillai
Director
114, 2c, 2nd floor, Rukminibai Market, Rukminibai Bldg No. 6, Pepper Orchard Lane, Mumbai - 400017.
pillaineeraj41@postvela.example
Should look same as the logo. Business card and Stationery should also be very professional.
TOVR Enterprise is the parent company underwhich many other firms are going to start. So back of the card should be designed in way that i can add the name of other firms.

```html
<!DOCTYPE html>
<html lang="en">
<head>
<meta charset="utf-8">
<title>TOVR Enterprise – Business Card</title>
<link rel="stylesheet" href="https://fonts.googleapis.com/css2?family=Open+Sans:wght@400;600;700&display=swap">
<style>
  :root {
    --bg: #e9e6e1;
    --card: #ffffff;
    --red: #d7182a;
    --red-dark: #b5101f;
    --red-light: #e63445;
    --ink: #1c1c1c;
    --text: #3a3a3a;
    --rule: #e4e4e4;
    --shadow: rgba(0,0,0,0.16);
  }
  * { margin: 0; padding: 0; box-sizing: border-box; }
  html, body {
    width: 1200px; height: 901px; overflow: hidden;
    background: var(--bg);
    font-family: "Open Sans", Arial, sans-serif;
  }
  .canvas { position: relative; width: 1200px; height: 901px; }
  .card {
    position: absolute; left: 300px;
    width: 600px; height: 343px;
    background: var(--card);
    border-radius: 22px;
    box-shadow: 0 10px 28px var(--shadow);
    overflow: hidden;
  }
  .card--back { top: 90px; }
  .card--front { top: 468px; }

  /* back side */
  .back-band {
    position: absolute; left: 0; top: 62px;
    width: 100%; height: 110px;
    background: linear-gradient(90deg, var(--red-dark) 0%, var(--red) 45%, var(--red-light) 100%);
  }
  .back-band::before, .back-band::after {
    content: ""; position: absolute; left: 0; width: 100%; height: 5px;
    background: var(--red-light); opacity: .65;
  }
  .back-band::before { top: 10px; }
  .back-band::after { bottom: 10px; }
  .wordmark {
    position: absolute; display: flex; align-items: center; gap: 10px;
    font-weight: 700; letter-spacing: 0.5px; white-space: nowrap;
  }
  .wordmark__dot { border-radius: 50%; flex: none; }
  .back-band .wordmark { left: 60px; top: 32px; color: #fff; font-size: 36px; gap: 12px; }
  .back-band .wordmark__dot { width: 40px; height: 40px; background: #fff; }

  /* front side */
  .card--front .wordmark { left: 30px; top: 154px; color: var(--red); font-size: 20px; }
  .card--front .wordmark__dot { width: 32px; height: 32px; background: var(--red); }
  .divider {
    position: absolute; left: 272px; top: 0; width: 1px; height: 100%;
    background: var(--rule);
  }
  .pointer {
    position: absolute; left: 272px; top: 48px;
    width: 0; height: 0;
    border-top: 16px solid transparent; border-bottom: 16px solid transparent;
    border-left: 16px solid var(--red);
  }
  .details { position: absolute; left: 300px; top: 44px; right: 16px; color: var(--text); }
  .details__name { font-size: 25px; font-weight: 700; color: var(--ink); line-height: 1.1; }
  .details__role { font-size: 13px; margin-top: 2px; }
  .details__address { font-size: 12px; line-height: 1.5; margin-top: 22px; white-space: nowrap; }
  .contacts { list-style: none; margin-top: 14px; }
  .contacts li { display: flex; align-items: center; gap: 10px; font-size: 13px; height: 22px; white-space: nowrap; }
  .contacts svg { width: 15px; height: 15px; flex: none; fill: var(--red); }
</style>
</head>
<body>
<div class="canvas">

  <section class="card card--back" aria-label="Business card, back">
    <div class="back-band">
      <div class="wordmark"><span class="wordmark__dot"></span>TOVR Enterprise</div>
    </div>
  </section>

  <section class="card card--front" aria-label="Business card, front">
    <div class="wordmark"><span class="wordmark__dot"></span>TOVR Enterprise</div>
    <div class="divider"></div>
    <div class="pointer"></div>
    <div class="details">
      <h1 class="details__name">Neeraj Pillai</h1>
      <p class="details__role">Director</p>
      <p class="details__address">114, 2c, 2nd floor, Rukminibai Market,<br>Rukminibai Bldg No. 6, Pepper Orchard Lane,<br>Mumbai - 400017.</p>
      <ul class="contacts">
        <li><svg viewBox="0 0 16 16" aria-hidden="true"><path d="M3.5 1.5l2.5 3-1.5 1.8c.8 1.8 2.2 3.2 4 4l1.8-1.5 3 2.5-1.2 2.2C7 13.5 2.5 9 1.3 2.7z"/></svg>+91 222 415 3062</li>
        <li><svg viewBox="0 0 16 16" aria-hidden="true"><path d="M4.5 1h7a1 1 0 011 1v12a1 1 0 01-1 1h-7a1 1 0 01-1-1V2a1 1 0 011-1zm.5 2v9h6V3zm3 10.2a.8.8 0 100-1.6.8.8 0 000 1.6z"/></svg>+91 982 640 2719</li>
        <li><svg viewBox="0 0 16 16" aria-hidden="true"><path d="M4 1h6l2 2v3H4zM2 7h12a1 1 0 011 1v5H1V8a1 1 0 011-1zm2 4v4h8v-4z"/></svg>+91 222 418 5907</li>
        <li><svg viewBox="0 0 16 16" aria-hidden="true"><path d="M8 1a7 7 0 100 14h3v-1.6H8A5.4 5.4 0 1113.4 8v.8c0 .7-.5 1.2-1.1 1.2s-1.1-.5-1.1-1.2V5h-1.5v.5A3.2 3.2 0 108 11.2c.9 0 1.8-.4 2.4-1 .4.8 1.1 1.2 1.9 1.2 1.5 0 2.7-1.2 2.7-2.7V8A7 7 0 008 1zm0 8.6a1.6 1.6 0 110-3.2 1.6 1.6 0 010 3.2z"/></svg>pillaineeraj41@postvela.example</li>
      </ul>
    </div>
  </section>

</div>
</body>
</html>
```